Website Header Design

Hi,

We're an electrical company that is looking for a new website header.
Our website is www.brambletonwiring.com
We are located in Toronto, Ontario, Canada.
We perform a lot of high rise electrical service work, snow melting system installation in garage ramps, and other general electrical work.
We're willing to change the size of the header and location/look of menus if needed but it is not required. We are hoping to keep our slogan if possible but having it in the header is not a make or break item. Whatever looks better.

Maybe the Toronto skyline could be incorporated somehow but the header also has to have some relevance to an electrical company.
I uploaded png files of the logo but I also have vector files available if needed

Target Market(s)

Property Managers, Contractors, Consulting Engineers

Industry/Entity Type

Electrical

Requirements
Must have
• Our Logo.
Nice to have
• Slogan
Should not have
• Flash

```html
<!DOCTYPE html>
<html lang="en">
<head>
<meta charset="utf-8">
<title>Brambleton Wiring — Header</title>
<link rel="stylesheet" href="https://fonts.googleapis.com/css2?family=Exo+2:wght@400;500&display=swap">
<style>
  :root {
    --bg-deep: #1c1c1c;
    --bg-mid: #3a3a3a;
    --bg-light: #5a5856;
    --accent: #f39322;
    --accent-soft: rgba(243, 147, 34, 0.35);
    --text: #ffffff;
    --nav-top: #3c3c3c;
    --nav-bottom: #1e1e1e;
    --divider: #9a9a9a;
    --icon: #a8a8a8;
    --flag-red: #e0262b;
  }
  * { margin: 0; padding: 0; box-sizing: border-box; }
  html, body {
    width: 1200px;
    height: 218px;
    overflow: hidden;
    background: var(--bg-deep);
  }
  .site-header {
    position: relative;
    width: 1200px;
    height: 218px;
    overflow: hidden;
    font-family: "Exo 2", sans-serif;
    color: var(--text);
  }
  .header-backdrop {
    position: absolute;
    inset: 0;
    background:
      radial-gradient(ellipse 420px 150px at 880px 120px, var(--accent-soft), transparent 70%),
      radial-gradient(ellipse 360px 200px at 820px 60px, rgba(255,255,255,0.18), transparent 70%),
      radial-gradient(ellipse 300px 160px at 1120px 150px, rgba(243,147,34,0.22), transparent 70%),
      linear-gradient(100deg, var(--bg-deep) 0%, var(--bg-mid) 45%, var(--bg-light) 70%, var(--bg-mid) 100%);
  }
  .brand {
    position: absolute;
    left: 120px;
    top: 62px;
    width: 190px;
    display: flex;
    flex-direction: column;
    align-items: center;
    gap: 14px;
  }
  .brand-mark {
    width: 44px;
    height: 44px;
    background: var(--accent);
  }
  .brand-name {
    font-size: 28px;
    font-weight: 500;
    line-height: 1.05;
    text-align: center;
    color: var(--text);
  }
  .slogan {
    position: absolute;
    left: 380px;
    top: 24px;
    font-size: 38px;
    font-weight: 400;
    line-height: 56px;
    text-align: center;
    letter-spacing: -0.3px;
  }
  .slogan span { display: block; }
  .utility-links {
    position: absolute;
    top: 14px;
    right: 23px;
    display: flex;
    gap: 10px;
  }
  .utility-links .icon {
    width: 23px;
    height: 23px;
    border-radius: 4px;
    background: var(--icon);
  }
  .utility-links .flag {
    width: 32px;
    height: 23px;
    border-radius: 0;
    background: linear-gradient(90deg, var(--flag-red) 0 25%, #fff 25% 75%, var(--flag-red) 75% 100%);
  }
  .main-nav {
    position: absolute;
    left: 306px;
    top: 160px;
    width: 770px;
    height: 58px;
    background: linear-gradient(180deg, var(--nav-top), var(--nav-bottom));
    display: flex;
    align-items: center;
    justify-content: center;
  }
  .main-nav ul {
    list-style: none;
    display: flex;
    align-items: center;
  }
  .main-nav li {
    font-size: 18px;
    font-weight: 400;
    color: var(--text);
  }
  .main-nav li.active { color: var(--accent); }
  .main-nav li + li::before {
    content: "|";
    color: var(--divider);
    margin: 0 28px;
  }
</style>
</head>
<body>
<header class="site-header">
  <div class="header-backdrop" role="img" aria-label="Dark background with sweeping orange and white light streaks suggesting flowing electricity"></div>

  <div class="brand">
    <div class="brand-mark"></div>
    <div class="brand-name">Brambleton<br>Wiring</div>
  </div>

  <p class="slogan"><span>Powerful Solutions.</span><span>Professional Service.</span></p>

  <div class="utility-links">
    <span class="icon flag" aria-label="Canada"></span>
    <span class="icon" aria-label="News feed"></span>
    <span class="icon" aria-label="Social page"></span>
    <span class="icon" aria-label="Social feed"></span>
  </div>

  <nav class="main-nav">
    <ul>
      <li class="active">HOME</li>
      <li>ABOUT US</li>
      <li>SERVICES</li>
      <li>PROJECTS</li>
      <li>CLIENTS</li>
      <li>CONTACTS</li>
    </ul>
  </nav>
</header>
</body>
</html>
```